Local Healthy meal delivery service needs a new flyer

Looking for a fresh and modern flyer design for a company called "Quillmarsh Fresh Co". We provide healthy and delicious meals to families, business offices and health care workers. We would like to see designs that communicate freshness, convenience, non contact delivery and customizable meal plan options. We would like to see designs that mirror our website colors, look and feel: quillmarshfreshco.com

Target Market(s)

Families, Business Offices, Health care workers

Requirements
Must have
• Color scheme and layout matching our brand and website
Our Logo
Modern clean/professional look
contact info: website, phone number, social media
Appropriate photos
Nice to have
• "How it Works" Summary

```html
<!DOCTYPE html>
<html lang="en">
<head>
<meta charset="utf-8">
<title>Quillmarsh Fresh Co – Flyer</title>
<link rel="stylesheet" href="https://fonts.googleapis.com/css2?family=Kaushan+Script&family=Roboto+Condensed:wght@400;700&family=Mulish:wght@400;700;800&display=swap">
<style>
:root{
  --green:#8cc63f;
  --green-dark:#6fa52a;
  --charcoal:#1e1f20;
  --charcoal-soft:#2d2e2f;
  --ink:#1a1a1a;
  --paper:#ffffff;
  --backdrop:#f2f2f2;
}
*{margin:0;padding:0;box-sizing:border-box}
html,body{width:1200px;height:1000px;overflow:hidden;background:var(--backdrop)}
.flyer{position:absolute;left:248px;top:28px;width:708px;height:917px;background:var(--paper);overflow:hidden;font-family:"Mulish",sans-serif;color:var(--ink)}
.hero{position:absolute;left:0;top:0;width:708px;height:360px;background:radial-gradient(circle at 30% 40%,#3a3b3c,var(--charcoal) 75%)}
.hero-stripe{position:absolute;left:0;top:360px;width:708px;height:10px;background:var(--green)}
.hero-photo-wrap{position:absolute;left:362px;top:0;width:346px;height:400px;filter:drop-shadow(0 10px 10px rgba(0,0,0,.35))}
.hero-photo{width:100%;height:100%;clip-path:polygon(0 0,100% 0,100% 100%,230px 100%,0 300px);background:linear-gradient(150deg,#171717 0%,#2a2a2a 40%,#7a2e28 62%,#b8564e 75%,#1d1d1d 100%)}
.brand{position:absolute;left:92px;top:50px;width:175px;display:flex;flex-direction:column;align-items:center;gap:10px}
.brand-dot{width:36px;height:36px;border-radius:50%;background:var(--green)}
.brand-name{font-family:"Roboto Condensed",sans-serif;font-weight:700;font-size:24px;color:var(--paper);text-align:center;line-height:1.05;text-transform:uppercase}
.headline{position:absolute;left:37px;top:168px;font-family:"Kaushan Script",cursive;color:var(--paper);font-size:40px;line-height:63px}
.headline-strong{position:absolute;left:38px;top:298px;font-family:"Roboto Condensed",sans-serif;font-weight:700;font-size:33px;color:var(--green);letter-spacing:-.3px}
.badge{position:absolute;left:382px;top:242px;width:102px;height:102px;border-radius:50%;background:var(--paper);border:4px solid #dcdcdc;transform:rotate(-12deg)}
.section-title{position:absolute;left:227px;top:372px;width:275px;height:42px}
.section-title span{position:absolute;inset:0;display:flex;align-items:center;justify-content:center;font-family:"Roboto Condensed",sans-serif;font-weight:700;font-size:28px;color:var(--green)}
.step{position:absolute;left:0;width:708px;height:80px}
.step-tab{position:absolute;left:0;top:0;width:106px;height:62px;background:var(--green);display:flex;align-items:center;justify-content:center}
.step-fold{position:absolute;left:76px;top:62px}
.step-text{position:absolute;left:138px;width:535px;font-size:13.2px;line-height:17px}
.step-text b{font-weight:800}
.food-strip{position:absolute;left:0;top:707px;width:432px;height:112px;display:flex}
.food-strip div{flex:1}
.food-1{background:linear-gradient(135deg,#7a4a1e,#d9a45a 50%,#5d6b2f)}
.food-2{background:linear-gradient(135deg,#3c5a24,#c9892a 45%,#9a2e1c 80%)}
.food-3{background:linear-gradient(135deg,#8a3e1c,#c86a2e 50%,#4f5a23)}
.accent-bar{position:absolute;left:685px;top:707px;width:23px;height:112px;background:var(--green)}
.values{position:absolute;left:468px;top:712px;font-family:"Roboto Condensed",sans-serif;font-weight:700;font-size:28.5px;line-height:35px;color:var(--green);white-space:nowrap}
.contact{position:absolute;left:0;top:832px;width:268px;height:85px}
.contact-body{position:absolute;left:25px;top:12px;color:var(--paper)}
.contact-title{font-family:"Roboto Condensed",sans-serif;font-weight:700;font-size:27px;line-height:30px}
.contact-line{display:flex;align-items:center;gap:7px;font-size:11.5px;font-weight:700;line-height:15px}
.footer-band{position:absolute;left:250px;top:890px;width:458px;height:27px;background:var(--charcoal)}
.signup{position:absolute;left:468px;top:834px;width:196px;height:70px;border:2px dashed var(--green);border-radius:12px;background:var(--paper);text-align:center}
.signup-title{font-family:"Roboto Condensed",sans-serif;font-weight:700;font-size:28px;line-height:30px;margin-top:3px;color:var(--ink)}
.signup-note{font-family:"Roboto Condensed",sans-serif;font-weight:700;font-size:8px;text-transform:uppercase}
.signup-url{display:inline-block;margin-top:4px;background:var(--green);color:var(--paper);font-size:11px;font-weight:800;border-radius:9px;padding:1px 12px}
</style>
</head>
<body>
<main class="flyer">
  <section class="hero">
    <div class="brand">
      <div class="brand-dot"></div>
      <div class="brand-name">Quillmarsh Fresh Co</div>
    </div>
    <p class="headline">Providing you<br>fresh, fully cooked,</p>
    <p class="headline-strong">READY TO EAT MEALS!</p>
  </section>
  <div class="hero-stripe"></div>
  <div class="hero-photo-wrap">
    <div class="hero-photo" role="img" aria-label="Sliced grilled steak on a slate board with cherry tomatoes, mushrooms and herbs"></div>
  </div>
  <div class="badge" role="img" aria-label="Certification seal"></div>

  <div class="section-title">
    <svg width="275" height="42" viewBox="0 0 275 42"><path d="M2 1 L22 40 H253 L273 1" fill="none" stroke="#8cc63f" stroke-width="1.5" stroke-dasharray="4 3"/></svg>
    <span>HOW IT WORKS</span>
  </div>

  <div class="step" style="top:420px">
    <div class="step-tab">
      <svg width="44" height="44" viewBox="0 0 44 44" fill="none" stroke="#fff" stroke-width="2"><rect x="13" y="6" width="22" height="30" rx="2"/><rect x="8" y="9" width="22" height="30" rx="2" fill="#8cc63f"/><path d="M13 20h12M13 25h12M13 30h9"/><text x="19" y="16" font-size="5" fill="#fff" stroke="none" text-anchor="middle" font-family="sans-serif">MENU</text></svg>
    </div>
    <svg class="step-fold" width="30" height="14"><path d="M0 0 H30 L30 14 Z" fill="#6fa52a"/></svg>
    <p class="step-text" style="top:19px"><b>Every Tuesday</b> we publish 2 menus for the following week, one for each delivery day (Tuesday and Thursday).</p>
  </div>

  <div class="step" style="top:507px">
    <div class="step-tab">
      <svg width="44" height="44" viewBox="0 0 44 44" fill="none" stroke="#fff" stroke-width="2" stroke-linecap="round"><path d="M4 10h6l5 18h18l4-12H13"/><circle cx="17" cy="35" r="2.5"/><circle cx="31" cy="35" r="2.5"/><circle cx="32" cy="10" r="7"/><path d="M28.5 10l2.5 2.5 4.5-5"/></svg>
    </div>
    <svg class="step-fold" width="30" height="14"><path d="M0 0 H30 L30 14 Z" fill="#6fa52a"/></svg>
    <p class="step-text" style="top:17px"><b>Place order</b> on our website by midnight on Saturday with meal plan and <b>choose your package, delivery day(s) and location.</b></p>
  </div>

  <div class="step" style="top:595px">
    <div class="step-tab">
      <svg width="48" height="44" viewBox="0 0 48 44" fill="none" stroke="#fff" stroke-width="2" stroke-linejoin="round"><path d="M8 16h32v22H8z"/><path d="M8 16l4-6h24l4 6"/><path d="M17 10c0-5 14-5 14 0"/><path d="M8 24h32M20 24v5h8v-5"/></svg>
    </div>
    <svg class="step-fold" width="30" height="14"><path d="M0 0 H30 L30 14 Z" fill="#6fa52a"/></svg>
    <p class="step-text" style="top:9px"><b>We drop off a blue soft cooler with your name on it to your specified delivery location</b> on the day you choose. Leave your empty cooler at the drop off location and we replace it with a fresh one on your next order.</p>
  </div>

  <div class="food-strip">
    <div class="food-1" role="img" aria-label="Roasted chicken with vegetables"></div>
    <div class="food-2" role="img" aria-label="Stir-fried peppers and vegetables"></div>
    <div class="food-3" role="img" aria-label="Baked flatbread with toppings"></div>
  </div>
  <div class="accent-bar"></div>
  <p class="values">LOCAL. FRESH.<br>ALL NATURAL.<br>NO ANTIBIOTICS.</p>

  <div class="footer-band"></div>
  <div class="contact">
    <svg width="268" height="85" viewBox="0 0 268 85" style="position:absolute;left:0;top:0"><path d="M0 0 H222 C240 0 244 14 250 30 L268 85 H0 Z" fill="#8cc63f"/></svg>
    <div class="contact-body">
      <p class="contact-title">GET IN TOUCH</p>
      <p class="contact-line"><svg width="9" height="9" viewBox="0 0 24 24"><path d="M6 2l4 5-2 3c1 3 3 5 6 6l3-2 5 4-3 4C10 21 3 14 2 5z" fill="#fff"/></svg>555-014-2290</p>
      <p class="contact-line"><svg width="10" height="8" viewBox="0 0 20 14"><rect x="1" y="1" width="18" height="12" fill="none" stroke="#fff" stroke-width="2"/><path d="M1 1l9 7 9-7" fill="none" stroke="#fff" stroke-width="2"/></svg>hello@quillmarshfreshco.com</p>
    </div>
  </div>

  <div class="signup">
    <p class="signup-title">SIGN UP NOW</p>
    <p class="signup-note">To have our menus delivered to you weekly!</p>
    <span class="signup-url">www.quillmarshfreshco.com</span>
  </div>
</main>
</body>
</html>
```